Flyer Design for Private Car Service

Flyer should cater to Business Travelers and Executives who travel Business Class or First Class.
Flyer should include images attached.
Flyer should include the below text
Dallas to Austin
Chauffeured SUVs
• Travel Dallas to Austin in a new 2025 Marlow Strider for $499 one-way
• Trip includes a Uniformed Chauffeur who has a Commercial Drivers License (CDL)
• You can Schedule Chauffeur Pickup at Your Home in Dallas
• Our Chauffeur will Drop You Off at Your Final Destination in Austin
• You can Schedule Chauffeur Return Pickup in Austin and Return Back to Dallas.
• We offer Faster Times on Door-to-Door Travel than Bluecrest Airways
• We offer Comparable Prices on Door-to-Door Travel Times than Bluecrest Airways
• All of our trips are insured with $500k of commercial auto insurance
• Our Passengers can Talk on Cell Phone & Conduct Quill calls Throughout Travel
• Our Passengers have Maximum Privacy, Comfort and First-Class Amenities.
• Our Passengers Avoid Harwick Vale Field and KPR Airport hassles & delays
• Member Brenton Chamber of Commerce, Larkmoor Chamber of Commerce.
• Book your trip today at www.ridemarquel.example
Target Market(s)
Business Travelers
Look and feel
Each slider illustrates characteristics of the customer's brand and the style your logo design should communicate.

```html
<!DOCTYPE html>
<html lang="en">
<head>
<meta charset="utf-8">
<title>Marquel – Dallas to Austin Flyer</title>
<link rel="stylesheet" href="https://fonts.googleapis.com/css2?family=PT+Serif:wght@400;700&family=Poppins:wght@400;600;700&display=swap">
<style>
  :root {
    --red: #d8362c;
    --red-soft: rgba(216, 54, 44, 0.55);
    --red-clear: rgba(216, 54, 44, 0);
    --ink: #1f1c1d;
    --slate: #444a50;
    --paper: #eeeeec;
    --stage: #e4e4e4;
    --footer: #221e1f;
    --white: #ffffff;
  }
  * { margin: 0; padding: 0; box-sizing: border-box; }
  html, body { width: 1200px; height: 1117px; overflow: hidden; background: var(--stage); }
  .flyer {
    position: absolute; left: 220px; top: 21px;
    width: 760px; height: 1074px;
    background: var(--paper);
    overflow: hidden;
    font-family: "Poppins", sans-serif;
    color: var(--ink);
  }
  .corner-accent { position: absolute; top: 47px; width: 177px; height: 125px; }
  .corner-left { left: 0; background: linear-gradient(90deg, var(--red-soft) 0%, var(--red-clear) 100%); }
  .corner-right { right: 0; background: linear-gradient(270deg, var(--red-soft) 0%, var(--red-clear) 100%); }
  .brand {
    position: absolute; top: 82px; left: 0; width: 100%;
    text-align: center;
    font-family: "PT Serif", serif; font-weight: 400;
    font-size: 40px; letter-spacing: 3px; color: var(--ink);
  }
  .headline {
    position: absolute; top: 160px; left: 0; width: 100%;
    text-align: center;
    font-family: "PT Serif", serif; font-weight: 700;
    font-size: 64px; color: var(--red); letter-spacing: 0.5px;
  }
  .subhead {
    position: absolute; top: 226px; left: 0; width: 100%;
    text-align: center;
    font-family: "PT Serif", serif; font-weight: 700;
    font-size: 32px; color: var(--slate);
  }
  .rule { position: absolute; height: 2px; background: var(--red); top: 249px; }
  .rule-left { left: 83px; width: 112px; }
  .rule-right { left: 565px; width: 122px; }
  .photo-fleet {
    position: absolute; top: 279px; left: 0; width: 100%; height: 230px;
    background: linear-gradient(180deg, #dcd2cc 0%, #c9c3bf 20%, #5a5a5c 45%, #3a3a3c 62%, #b9aeaa 80%, var(--paper) 100%);
  }
  .photo-team {
    position: absolute; top: 780px; left: 351px; width: 409px; height: 226px;
    background: linear-gradient(180deg, var(--paper) 0%, #9a9898 40%, #2f2d2e 75%, #1f1d1e 100%);
  }
  .photo-arrival {
    position: absolute; top: 846px; left: 0; width: 351px; height: 160px;
    background: linear-gradient(180deg, var(--paper) 0%, #c9cacc 30%, #3c3c3e 75%, #262426 100%);
  }
  .offer { position: absolute; left: 52px; width: 191px; text-align: center; }
  .offer-lead { top: 518px; font-weight: 600; font-size: 17px; line-height: 21px; }
  .price {
    position: absolute; left: 52px; width: 191px; text-align: center;
    color: var(--red); font-weight: 700; line-height: 1;
  }
  .price sup { font-size: 0.34em; vertical-align: top; position: relative; top: 0.25em; }
  .price-trip { top: 585px; font-size: 74px; letter-spacing: -2px; }
  .price-note {
    position: absolute; top: 645px; left: 52px; width: 172px; text-align: right;
    color: var(--red); font-weight: 700; font-size: 17px;
  }
  .offer-divider { position: absolute; top: 681px; left: 52px; width: 189px; height: 2px; background: var(--red); }
  .offer-insured { top: 697px; font-weight: 600; font-size: 17px; line-height: 21px; }
  .price-insured { top: 740px; font-size: 76px; letter-spacing: -2px; }
  .insured-note {
    position: absolute; top: 822px; left: 42px; width: 211px; text-align: center;
    color: var(--red); font-weight: 700; font-size: 15px; line-height: 18px;
    z-index: 1;
  }
  .benefits { position: absolute; top: 522px; list-style: none; width: 210px; }
  .benefits-a { left: 286px; }
  .benefits-b { left: 522px; }
  .benefits li {
    position: relative; padding-left: 20px; margin-bottom: 12px;
    font-size: 11px; line-height: 13px; color: #2b2b2b;
  }
  .tick { position: absolute; left: 0; top: 1px; width: 10px; height: 10px; }
  .footer {
    position: absolute; left: 0; bottom: 0; width: 100%; height: 68px;
    background: var(--footer);
    display: flex; align-items: center; justify-content: center; gap: 18px;
  }
  .footer-cta { color: var(--white); font-weight: 600; font-size: 21px; }
  .footer-url {
    background: var(--red); color: var(--white); font-weight: 600; font-size: 20px;
    padding: 2px 16px; border-radius: 18px;
  }
</style>
</head>
<body>
<main class="flyer">
  <div class="corner-accent corner-left" role="img" aria-label="Red decorative accent in the top left corner"></div>
  <div class="corner-accent corner-right" role="img" aria-label="Red decorative accent in the top right corner"></div>

  <div class="brand">MARQUEL</div>

  <h1 class="headline">DALLAS TO AUSTIN</h1>
  <span class="rule rule-left"></span>
  <h2 class="subhead">CHAUFFEURED SUVS</h2>
  <span class="rule rule-right"></span>

  <div class="photo-fleet" role="img" aria-label="Uniformed chauffeurs standing beside black, white and red SUVs in front of a building"></div>
  <div class="photo-arrival" role="img" aria-label="Chauffeur opening the door of a black SUV for a business passenger"></div>
  <div class="photo-team" role="img" aria-label="Three uniformed chauffeurs in caps and dark jackets"></div>

  <p class="offer offer-lead">Travel Dallas to Austin in a new 2025 Marlow Strider for</p>
  <p class="price price-trip"><sup>$</sup>499</p>
  <p class="price-note">one-way</p>
  <span class="offer-divider"></span>
  <p class="offer offer-insured">All of our trips are insured with</p>
  <p class="price price-insured"><sup>$</sup>500k</p>
  <p class="insured-note">of commercial auto insurance</p>

  <ul class="benefits benefits-a">
    <li><svg class="tick" viewBox="0 0 10 10"><circle cx="5" cy="5" r="5" fill="#d8362c"/><path d="M2.6,5.2 L4.3,6.8 L7.4,3.4" stroke="#fff" stroke-width="1.4" fill="none"/></svg>Trip includes a Uniformed Chauffeur who has a Commercial Drivers License (CDL)</li>
    <li><svg class="tick" viewBox="0 0 10 10"><circle cx="5" cy="5" r="5" fill="#d8362c"/><path d="M2.6,5.2 L4.3,6.8 L7.4,3.4" stroke="#fff" stroke-width="1.4" fill="none"/></svg>You can Schedule Chauffeur Pickup at Your Home in Dallas</li>
    <li><svg class="tick" viewBox="0 0 10 10"><circle cx="5" cy="5" r="5" fill="#d8362c"/><path d="M2.6,5.2 L4.3,6.8 L7.4,3.4" stroke="#fff" stroke-width="1.4" fill="none"/></svg>Our Chauffeur will Drop You Off at Your Final Destination in Austin</li>
    <li><svg class="tick" viewBox="0 0 10 10"><circle cx="5" cy="5" r="5" fill="#d8362c"/><path d="M2.6,5.2 L4.3,6.8 L7.4,3.4" stroke="#fff" stroke-width="1.4" fill="none"/></svg>You can Schedule Chauffeur Return Pickup in Austin and Return Back to Dallas.</li>
    <li><svg class="tick" viewBox="0 0 10 10"><circle cx="5" cy="5" r="5" fill="#d8362c"/><path d="M2.6,5.2 L4.3,6.8 L7.4,3.4" stroke="#fff" stroke-width="1.4" fill="none"/></svg>We offer Faster Times on Door-to-Door Travel than Bluecrest Airways</li>
  </ul>

  <ul class="benefits benefits-b">
    <li><svg class="tick" viewBox="0 0 10 10"><circle cx="5" cy="5" r="5" fill="#d8362c"/><path d="M2.6,5.2 L4.3,6.8 L7.4,3.4" stroke="#fff" stroke-width="1.4" fill="none"/></svg>We offer Comparable Prices on Door-to-Door Travel Times than Bluecrest Airways</li>
    <li><svg class="tick" viewBox="0 0 10 10"><circle cx="5" cy="5" r="5" fill="#d8362c"/><path d="M2.6,5.2 L4.3,6.8 L7.4,3.4" stroke="#fff" stroke-width="1.4" fill="none"/></svg>Our Passengers can Talk on Cell Phone &amp; Conduct Quill calls Throughout Travel</li>
    <li><svg class="tick" viewBox="0 0 10 10"><circle cx="5" cy="5" r="5" fill="#d8362c"/><path d="M2.6,5.2 L4.3,6.8 L7.4,3.4" stroke="#fff" stroke-width="1.4" fill="none"/></svg>Our Passengers have Maximum Privacy, Comfort and First-Class Amenities.</li>
    <li><svg class="tick" viewBox="0 0 10 10"><circle cx="5" cy="5" r="5" fill="#d8362c"/><path d="M2.6,5.2 L4.3,6.8 L7.4,3.4" stroke="#fff" stroke-width="1.4" fill="none"/></svg>Our Passengers Avoid Harwick Vale Field and KPR Airport hassles &amp; delays</li>
    <li><svg class="tick" viewBox="0 0 10 10"><circle cx="5" cy="5" r="5" fill="#d8362c"/><path d="M2.6,5.2 L4.3,6.8 L7.4,3.4" stroke="#fff" stroke-width="1.4" fill="none"/></svg>Member Brenton Chamber of Commerce, Larkmoor Chamber of Commerce.</li>
  </ul>

  <footer class="footer">
    <span class="footer-cta">Book your trip today at</span>
    <span class="footer-url">www.ridemarquel.example</span>
  </footer>
</main>
</body>
</html>
```